Special Educational Conference Poster

Looking for a poster that I can use electronically more than anything - to post on Chatterbook \ social media. Should be bold, eye catching, and within our brand colors.

3rd Annual Young Learners Beyond Limits Summit
Featuring Dr. Martin Ellery
Lighting the Way: Growing Courage, Drive, and Grit in Every Young Learner Who Thinks Differently

Friday, May 10, 2019, 9am - 3pm

The Linden Grove Academy at Fenwick opens our campus to teachers, parents, and practitioners from the Delaware Valley to learn together on how to support the extraordinary students in our lives. The conference runs from 9am - 3pm and lunch is included. This event is free and open to the public, but registration is required.

Link to registration: https://www.lindengroveacad.org/admissions/admissions-visit-and-events

```html
<!DOCTYPE html>
<html lang="en">
<head>
<meta charset="utf-8">
<title>Young Learners Beyond Limits Summit</title>
<link rel="stylesheet" href="https://fonts.googleapis.com/css2?family=Fredoka:wght@500;600&family=Questrial&family=Baloo+2:wght@700;800&display=swap">
<style>
  :root {
    --grass-deep: #2f4a1c;
    --grass-mid: #5f7f34;
    --grass-light: #8fa85a;
    --bark: #3a2a22;
    --warm-light: #d9b89a;
    --brand-teal: #1aa7c9;
    --brand-green: #2fb06a;
    --band-green: #33b56b;
    --band-green-light: #4cc27a;
    --accent-red: #e8123a;
    --sub-yellow: #e6f03a;
    --ink: #111111;
    --white: #ffffff;
    --silver: #c9c9c9;
  }
  html, body {
    margin: 0;
    padding: 0;
    overflow: hidden;
    background: #ffffff;
  }
  .poster {
    position: relative;
    width: 1200px;
    height: 720px;
    overflow: hidden;
    font-family: "Questrial", sans-serif;
  }
  .poster__photo {
    position: absolute;
    inset: 0;
    background:
      radial-gradient(ellipse 340px 300px at 860px 400px, var(--warm-light) 0%, rgba(217,184,154,0.55) 45%, rgba(217,184,154,0) 75%),
      radial-gradient(ellipse 500px 220px at 300px 120px, var(--bark) 0%, rgba(58,42,34,0) 80%),
      linear-gradient(180deg, #3b3a2a 0%, var(--grass-deep) 28%, var(--grass-mid) 55%, var(--grass-light) 80%, var(--grass-mid) 100%);
  }
  .poster__shapes {
    position: absolute;
    inset: 0;
  }
  .brand {
    position: absolute;
    left: 44px;
    top: 62px;
    display: flex;
    align-items: center;
    gap: 10px;
    font-family: "Questrial", sans-serif;
    font-size: 29px;
    line-height: 1;
    color: var(--brand-teal);
    white-space: nowrap;
  }
  .brand__dot {
    width: 18px;
    height: 18px;
    border-radius: 50%;
    background: var(--brand-green);
  }
  .kicker {
    position: absolute;
    left: 444px;
    top: 52px;
    margin: 0;
    font-family: "Fredoka", sans-serif;
    font-weight: 600;
    font-size: 78px;
    line-height: 1;
    color: var(--accent-red);
    -webkit-text-stroke: 6px var(--white);
    paint-order: stroke fill;
    letter-spacing: -1px;
  }
  .title {
    position: absolute;
    left: 48px;
    top: 184px;
    margin: 0;
    font-family: "Fredoka", sans-serif;
    font-weight: 600;
    font-size: 46px;
    line-height: 1;
    color: var(--ink);
    -webkit-text-stroke: 5px var(--white);
    paint-order: stroke fill;
    white-space: nowrap;
  }
  .speaker {
    position: absolute;
    left: 48px;
    top: 238px;
    margin: 0;
    font-family: "Baloo 2", sans-serif;
    font-weight: 700;
    font-size: 21px;
    line-height: 1;
    color: var(--white);
    letter-spacing: 0.5px;
  }
  .theme {
    position: absolute;
    left: 48px;
    top: 268px;
    width: 682px;
    margin: 0;
    font-size: 26px;
    line-height: 32px;
    letter-spacing: 1.6px;
    color: var(--sub-yellow);
  }
  .intro {
    position: absolute;
    left: 44px;
    top: 374px;
    width: 686px;
    margin: 0;
    font-size: 20px;
    line-height: 26.5px;
    color: var(--white);
    text-align: justify;
    letter-spacing: 0.4px;
  }
  .date {
    position: absolute;
    left: 44px;
    top: 600px;
    margin: 0;
    font-family: "Baloo 2", sans-serif;
    font-weight: 800;
    font-size: 46px;
    line-height: 1;
    color: var(--accent-red);
    -webkit-text-stroke: 5px var(--white);
    paint-order: stroke fill;
    letter-spacing: -1px;
    white-space: nowrap;
  }
  .registration {
    position: absolute;
    left: 47px;
    top: 662px;
    margin: 0;
    font-family: "Baloo 2", sans-serif;
    font-weight: 700;
    font-size: 25px;
    line-height: 1;
    color: var(--white);
    white-space: nowrap;
  }
  .registration__link {
    color: var(--white);
    text-decoration: none;
    margin-left: 6px;
  }
</style>
</head>
<body>
  <main class="poster">
    <div class="poster__photo" role="img" aria-label="Photograph of a smiling young girl with long blonde hair lying on green grass, chin resting in her hands, garden blurred behind her"></div>

    <svg class="poster__shapes" width="1200" height="720" viewBox="0 0 1200 720" aria-hidden="true">
      <defs>
        <linearGradient id="band" x1="0" y1="0" x2="0" y2="1">
          <stop offset="0" stop-color="#33b56b"/>
          <stop offset="1" stop-color="#4cc27a"/>
        </linearGradient>
      </defs>
      <ellipse cx="150" cy="46" rx="248" ry="130" fill="#c9c9c9"/>
      <ellipse cx="144" cy="40" rx="240" ry="124" fill="#f4f4f4"/>
      <path d="M0 548 C 260 528, 560 560, 800 610 C 960 642, 1100 628, 1200 592 L1200 720 L0 720 Z" fill="#c9c9c9"/>
      <path d="M0 556 C 260 536, 560 568, 800 618 C 960 650, 1100 636, 1200 600 L1200 720 L0 720 Z" fill="#ffffff"/>
      <path d="M0 566 C 260 548, 560 580, 800 632 C 960 664, 1100 650, 1200 612 L1200 720 L0 720 Z" fill="url(#band)"/>
    </svg>

    <div class="brand">
      <span class="brand__dot"></span>
      <span class="brand__name">Verdalis Pharmacy</span>
    </div>

    <h2 class="kicker">3rd Annual</h2>
    <h1 class="title">Young Learners Beyond Limits Summit</h1>
    <p class="speaker">Featuring Dr. Martin Ellery</p>

    <p class="theme">Lighting the Way: Growing Courage, Drive, and Grit in Every Young Learner Who Thinks Differently</p>

    <p class="intro">The Linden Grove Academy at Fenwick opens our campus to teachers, parents, and practitioners from the Delaware Valley to learn together on how to support the extraordinary students in our lives. The conference runs from 9am - 3pm and lunch is included. This event is free and open to the public, but registration is required.</p>

    <p class="date">Friday, May 10, 2019, 9am - 3pm</p>

    <p class="registration">Link to registration: <a class="registration__link" href="https://www.lindengroveacad.org/admissions/admissions-visit-and-events">https://www.lindengroveacad.org/admissions/admissions-visit-and-events</a></p>
  </main>
</body>
</html>
```